KELO Logistics App for American company. Will be like Zimo freight but more grassroots

We need a logistics App, similar to a truck broker. Similar to the Zimo or Pask apps where a truck driver can connect with companies and pick up the freight to get paid. The company is called KELO after the Morroxan explorer Sahl Qoremmi. Zimo freight has an app can be similar but more driver focused.

Target Market(s)

Everyone who needs freight moved from one place to next

Industry/Entity Type

Trucking

Requirements
Must have
• GPS and easy to use interface between driver and companies
Nice to have
• Colors that are travel like and friendly
Should not have
• Be boring or plain or hard to understand

```html
<!DOCTYPE html>
<html lang="en">
<head>
<meta charset="utf-8">
<title>KELO Logistics App</title>
<link rel="stylesheet" href="https://fonts.googleapis.com/css2?family=Open+Sans:wght@400;600&family=Ubuntu:wght@400;500&display=swap">
<style>
:root{
  --orange:#f5652d;
  --black:#151515;
  --white:#ffffff;
  --gray-bg:#f1f1f1;
  --ink:#1c1c1c;
  --line:#e3e3e3;
  --placeholder-top:#8b909a;
  --placeholder-bottom:#5d626c;
}
*{box-sizing:border-box;margin:0;padding:0}
html,body{width:1200px;height:735px;overflow:hidden;background:#fff}
body{position:relative;font-family:"Ubuntu",sans-serif;color:var(--ink)}

.panel{position:absolute;top:79px;width:282px;height:609px;overflow:hidden}

/* Brand panel */
.brand-panel{left:73px;font-family:"Open Sans",sans-serif}
.brand-photo{position:absolute;inset:0;background:linear-gradient(180deg,var(--placeholder-top),var(--placeholder-bottom))}
.brand-copy{position:absolute;left:19px;top:52px;color:var(--white)}
.brand-name{font-size:34px;font-weight:400;letter-spacing:.5px;line-height:44px}
.brand-tagline{font-size:22px;line-height:28px;margin-top:2px}

/* Shared screen parts */
.screen{background:var(--black)}
.screen-title{color:var(--white);font-size:19px;font-weight:500;text-align:center;line-height:24px;height:82px;display:flex;align-items:center;justify-content:center}
.screen-body{position:absolute;left:11px;right:11px;top:82px;bottom:45px;background:var(--white);overflow:hidden}
.tab-bar{position:absolute;left:0;right:0;bottom:0;height:45px;background:var(--orange);display:flex;justify-content:space-around;align-items:center;color:var(--white);font-size:10.5px}
.tab{display:flex;flex-direction:column;align-items:center;gap:2px;width:60px}
.tab svg{width:15px;height:15px;fill:var(--white)}
.price{color:var(--orange);font-size:21px;font-weight:500}
.deadhead{font-size:9.5px;color:#333}
.deadhead b{font-weight:400;margin-right:8px}

/* Search screen */
.search-screen{left:450px;top:86px;width:291px;height:604px}
.search-screen .screen-body{left:12px;right:12px;bottom:41px}
.search-screen .tab-bar{height:41px}
.week-head{height:109px;text-align:center}
.week-title{font-size:19px;padding-top:17px;position:relative}
.fav{position:absolute;right:6px;top:20px;width:20px;height:18px}
.week{display:flex;justify-content:space-around;padding:13px 10px 0;font-size:12px}
.day{display:flex;flex-direction:column;align-items:center;gap:7px;width:24px}
.day span:last-child{color:#888;width:22px;height:22px;line-height:22px;border-radius:50%}
.day.active span:last-child{background:var(--orange);color:var(--white)}
.filter-bar{background:var(--gray-bg);height:94px;padding:15px 20px 0 19px}
.search-pill{background:var(--white);border-radius:20px;height:39px;display:flex;align-items:center;padding:0 14px;position:relative}
.search-pill svg{width:18px;height:18px}
.search-label{position:absolute;left:0;right:0;text-align:center;font-size:10.5px;color:#666;line-height:14px}
.search-label strong{display:block;font-size:13px;color:var(--ink);font-weight:500}
.sort-row{display:flex;justify-content:space-between;margin:14px -6px 0 -1px;font-size:12.5px}
.sort-row .sort{color:var(--orange)}
.load-card{padding:18px 11px 0 14px;height:188px;border-bottom:1px solid var(--line)}
.load-top{display:flex;justify-content:space-between;align-items:flex-start}
.load-meta{text-align:right;font-size:10px;color:#444;line-height:14px}
.load-card .deadhead{margin-top:24px}
.route{margin-top:9px;padding-left:18px;position:relative}
.route::before{content:"";position:absolute;left:4px;top:12px;height:39px;border-left:1px solid #999}
.stop{position:relative;margin-bottom:12px}
.stop::before{content:"";position:absolute;left:-18px;top:8px;width:7px;height:7px;background:var(--black)}
.stop:first-child::before{border-radius:50%}
.stop-city{font-size:13.5px}
.stop-time{font-size:7.5px;color:#444;margin-top:1px}
.hint{height:36px;line-height:36px;text-align:center;font-size:9.5px;box-shadow:0 2px 6px rgba(0,0,0,.08);border-bottom:1px solid var(--line)}
.load-card.peek{height:80px;border:0;padding-top:14px}

/* Details screen */
.details-screen{left:817px}
.details-bar{height:42px;display:flex;align-items:center;justify-content:space-between;padding:0 8px 0 9px;font-size:15.5px}
.details-bar svg{width:22px;height:18px;fill:none;stroke:var(--black);stroke-width:1.5}
.map{height:230px;background:linear-gradient(135deg,#e3e3e3,#c9c9c9 50%,#dcdcdc)}
.details-body{padding:17px 0 0 13px}
.details-body .deadhead{margin-top:15px;display:flex;align-items:center}
.details-body .deadhead::after{content:"";flex:1;border-top:1px solid var(--line);margin-left:2px}
.pickup{position:relative;padding:8px 14px 0 18px}
.pickup::before{content:"";position:absolute;left:2px;top:14px;bottom:-8px;border-left:1px solid #aaa}
.pickup::after{content:"";position:absolute;left:-1px;top:30px;width:7px;height:7px;border-radius:50%;background:var(--black)}
.pickup-title{color:var(--orange);font-size:13.5px;display:flex;justify-content:space-between}
.pickup-info{font-size:10px;color:#444;line-height:13px;margin-top:6px}
.rating{font-size:10px;color:#444;margin:10px 0 0 18px}
.rating .star{color:#f7b500}
.book-btn{display:block;margin:11px 0 0 18px;width:199px;height:35px;background:var(--orange);color:var(--white);font-size:14px;text-align:center;line-height:35px}
</style>
</head>
<body>

<section class="panel brand-panel">
  <div class="brand-photo" role="img" aria-label="Photo of a semi truck driving on a highway at sunset"></div>
  <div class="brand-copy">
    <h1 class="brand-name">KELO</h1>
    <p class="brand-tagline">Sed ut perspiciatis<br>unde omnis iste<br>natus</p>
  </div>
</section>

<section class="panel screen search-screen">
  <h2 class="screen-title">Easily Search Our<br>exclusive loadboard</h2>
  <div class="screen-body">
    <div class="week-head">
      <div class="week-title">Book
        <svg class="fav" viewBox="0 0 20 18"><path d="M10 17 2 9.5A4.6 4.6 0 0 1 10 3.5a4.6 4.6 0 0 1 8 6Z" fill="#151515"/><circle cx="16.5" cy="3" r="3" fill="#f5652d"/></svg>
      </div>
      <div class="week">
        <div class="day"><span>M</span><span>12</span></div>
        <div class="day active"><span>T</span><span>13</span></div>
        <div class="day"><span>W</span><span>14</span></div>
        <div class="day"><span>T</span><span>15</span></div>
        <div class="day"><span>F</span><span>16</span></div>
        <div class="day"><span>S</span><span>17</span></div>
        <div class="day"><span>S</span><span>18</span></div>
      </div>
    </div>
    <div class="filter-bar">
      <div class="search-pill">
        <svg viewBox="0 0 18 18" fill="none" stroke="#151515" stroke-width="1.6"><circle cx="7.5" cy="7.5" r="6"/><path d="m12 12 5 5"/></svg>
        <div class="search-label">All Loads<strong>Near You</strong></div>
      </div>
      <div class="sort-row"><span>Today</span><span class="sort">Sort: Deadhead</span></div>
    </div>
    <article class="load-card">
      <div class="load-top"><span class="price">$330</span><span class="load-meta">Van/Reefer.48.5k lbs<br>206 mi total</span></div>
      <p class="deadhead"><b>5 mi</b>deadhead</p>
      <div class="route">
        <div class="stop"><div class="stop-city">Houston, TX</div><div class="stop-time">Jan 28, 10:30 CST</div></div>
        <div class="stop"><div class="stop-city">San Antonio, TX</div><div class="stop-time">Jan 28, 10:30 CST</div></div>
      </div>
    </article>
    <div class="hint">Like loads you've previously hauled</div>
    <article class="load-card peek">
      <div class="load-top"><span class="price">$330</span><span class="load-meta">Van/Reefer.48.5k lbs<br>25 mi total</span></div>
    </article>
  </div>
  <nav class="tab-bar">
    <div class="tab"><svg viewBox="0 0 16 16" fill="none" stroke="#fff" stroke-width="1.5"><circle cx="7" cy="7" r="5.5"/><path d="m11 11 4 4"/></svg>Book</div>
    <div class="tab"><svg viewBox="0 0 16 16"><rect x="1" y="8" width="6" height="7"/><rect x="9" y="8" width="6" height="7"/><rect x="5" y="1" width="6" height="6"/></svg>My Loads</div>
    <div class="tab"><svg viewBox="0 0 16 16"><circle cx="8" cy="4" r="3"/><circle cx="3" cy="6" r="2.2"/><circle cx="13" cy="6" r="2.2"/><path d="M3 15a5 5 0 0 1 10 0ZM0 14a3 3 0 0 1 4-3l-1 3ZM16 14a3 3 0 0 0-4-3l1 3Z"/></svg>Drivers</div>
    <div class="tab"><svg viewBox="0 0 16 16"><circle cx="8" cy="4.5" r="3.5"/><path d="M1 16a7 6 0 0 1 14 0Z"/></svg>Account</div>
  </nav>
</section>

<section class="panel screen details-screen">
  <h2 class="screen-title">View full<br>load details</h2>
  <div class="screen-body">
    <div class="details-bar">
      <svg viewBox="0 0 22 18"><path d="M21 9H2M9 2 2 9l7 7"/></svg>
      <span>Load Details</span>
      <svg viewBox="0 0 22 18"><path d="M4 12V9a7 7 0 0 1 14 0v3"/><rect x="3" y="10" width="3" height="6" fill="#151515"/><rect x="16" y="10" width="3" height="6" fill="#151515"/></svg>
    </div>
    <div class="map" role="img" aria-label="Grey street map with an orange marker at the pickup location"></div>
    <div class="details-body">
      <span class="price">$330</span>
      <p class="deadhead"><b>5 mi</b>deadhead</p>
      <div class="pickup">
        <div class="pickup-title"><span>Pickup</span><span style="color:#666">&#8250;</span></div>
        <p class="pickup-info">Mon Jan, 01:30 CST<br>Dallas, TX</p>
      </div>
      <p class="rating">4.8 <span class="star">&#9733;</span> Fresh Spring inc.</p>
      <span class="book-btn">Book Load</span>
    </div>
  </div>
  <nav class="tab-bar">
    <div class="tab"><svg viewBox="0 0 16 16" fill="none" stroke="#fff" stroke-width="1.5"><circle cx="7" cy="7" r="5.5"/><path d="m11 11 4 4"/></svg>Book</div>
    <div class="tab"><svg viewBox="0 0 16 16"><rect x="1" y="8" width="6" height="7"/><rect x="9" y="8" width="6" height="7"/><rect x="5" y="1" width="6" height="6"/></svg>My Loads</div>
    <div class="tab"><svg viewBox="0 0 16 16"><circle cx="8" cy="4" r="3"/><circle cx="3" cy="6" r="2.2"/><circle cx="13" cy="6" r="2.2"/><path d="M3 15a5 5 0 0 1 10 0ZM0 14a3 3 0 0 1 4-3l-1 3ZM16 14a3 3 0 0 0-4-3l1 3Z"/></svg>Drivers</div>
    <div class="tab"><svg viewBox="0 0 16 16"><circle cx="8" cy="4.5" r="3.5"/><path d="M1 16a7 6 0 0 1 14 0Z"/></svg>Account</div>
  </nav>
</section>

</body>
</html>
```